Pebbleton Default Template Pages

I have a logo designed for my web and mobile based app. I would like a set of matching templates designed to present the various types of content the app will deliver to users. Please design for me a set of html and css based templates to present the web based content.
The chosen template designs will have a colour scheme complimentary to my existing Pebbleton logo. I have attached the Pebbleton Logo.

```html
<!DOCTYPE html>
<html lang="en">
<head>
<meta charset="utf-8">
<title>Pebbleton</title>
<link rel="stylesheet" href="https://fonts.googleapis.com/css2?family=Lato:wght@300;400;700;900&family=Quicksand:wght@500;600;700&display=swap">
<style>
:root{
  --blue:#0e62a9;
  --blue-dark:#1b4f96;
  --date-blue:#2c5fa5;
  --yellow:#f0b500;
  --olive:#c8c200;
  --green:#22b20e;
  --news-bg:#e9f0f7;
  --text:#1a1a1a;
  --white:#ffffff;
  --red-date:#d3222a;
}
*{margin:0;padding:0;box-sizing:border-box}
html,body{width:1200px;height:2446px;overflow:hidden}
body{position:relative;font-family:'Lato',sans-serif;color:var(--text);background:#fff}
.rainbow{position:absolute;left:0;width:1200px;height:8px;background:linear-gradient(90deg,#e5262c,#9b3a9a,#2a5caa,#1f9ad7,#27b24a,#f2c500,#f28a00,#8cc63f)}
.rainbow.top{top:0}
.rainbow.bottom{bottom:0}

/* header */
.site-header{position:absolute;top:8px;left:0;width:1200px;height:80px;background:#fff;box-shadow:0 3px 8px rgba(0,0,0,.15);z-index:3}
.nav-link{position:absolute;top:32px;font-size:16px;color:#222}
.btn-contact{position:absolute;left:966px;top:23px;width:122px;height:38px;background:var(--olive);color:#fff;font-size:16px;font-weight:700;display:flex;align-items:center;justify-content:center}
.brand-badge{position:absolute;left:516px;top:4px;width:168px;height:168px;border-radius:50%;background:#fff;box-shadow:0 4px 8px rgba(0,0,0,.18);z-index:4;display:flex;flex-direction:column;align-items:center;justify-content:center;padding-top:20px}
.brand-dot{width:40px;height:40px;border-radius:50%;background:var(--blue-dark);margin-bottom:10px}
.brand-name{font-family:'Quicksand',sans-serif;font-weight:700;font-size:25px;color:var(--blue-dark)}

/* hero */
.hero{position:absolute;top:88px;left:0;width:1200px;height:595px;background:linear-gradient(180deg,#8fb3d4 0%,#c6d8e6 35%,#e7e4da 55%,#b59a6a 82%,#8c7440 100%)}
.hero-title{position:absolute;top:202px;left:0;width:1200px;text-align:center;font-size:53px;font-weight:700;color:#111}
.btn-start{position:absolute;left:523px;top:285px;width:154px;height:50px;background:linear-gradient(90deg,var(--green),#e0bd00);color:#fff;font-size:18px;font-weight:700;display:flex;align-items:center;justify-content:center}

/* categories */
.section-title{position:absolute;left:0;width:1200px;text-align:center;font-size:43px;font-weight:700;color:#111}
.tab{position:absolute;top:804px;height:38px;color:#fff;font-size:16px;font-weight:700;display:flex;align-items:center;justify-content:center;background:var(--yellow)}
.tab.active{background:linear-gradient(90deg,var(--green),#e6bd00)}
.card{position:absolute;top:881px;width:291px;height:443px;background:#fff;box-shadow:0 6px 14px rgba(240,181,0,.18)}
.card.featured{background:var(--yellow)}
.card-photo{position:absolute;left:0;top:0;width:291px;height:230px}
.card-body{position:absolute;left:11px;top:198px;width:269px;height:231px;background:#fff;box-shadow:0 2px 8px rgba(0,0,0,.1);text-align:center;padding-top:24px}
.card-date{font-size:16px;font-weight:700;color:var(--date-blue);margin-bottom:10px}
.card-text{font-size:16px;font-weight:400;line-height:29px;color:#222;padding:0 26px}
.card-more{display:inline-block;margin-top:12px;font-size:16px;font-weight:700;color:var(--blue-dark);text-decoration:underline}
.arrow{position:absolute;top:1098px;width:26px;height:26px}

/* news */
.news{position:absolute;top:1389px;left:0;width:1200px;height:654px;background:var(--news-bg)}
.news-main{position:absolute;left:111px;top:1509px;width:546px;height:468px;background:#fff}
.news-main-photo{width:546px;height:408px;background:linear-gradient(135deg,#e9dccd,#c8a98c 45%,#6b5a4c 75%,#2d2a2a)}
.news-main-caption{padding:22px 19px;font-size:15px;font-weight:700;color:#111}
.news-item{position:absolute;left:702px;width:386px;height:109px;background:#fff}
.news-thumb{position:absolute;left:8px;top:6px;width:194px;height:98px}
.news-date{position:absolute;left:218px;top:23px;font-size:12px;color:var(--red-date)}
.news-head{position:absolute;left:218px;top:48px;font-size:13px;font-weight:700;color:#111}
.news-more{position:absolute;left:219px;top:75px;font-size:11px;color:#444;text-decoration:underline}

/* footer */
.site-footer{position:absolute;top:2043px;left:0;width:1200px;height:395px;background:var(--blue)}
.footer-brand{position:absolute;left:176px;top:2155px;width:160px;display:flex;flex-direction:column;align-items:center}
.footer-brand .dot{width:86px;height:86px;border-radius:50%;background:#fff;margin-bottom:16px}
.footer-brand .name{font-family:'Quicksand',sans-serif;font-weight:700;font-size:34px;color:var(--white)}
.footer-col{position:absolute;top:2098px;color:var(--white)}
.footer-col h3{font-family:'Lato',sans-serif;font-size:21px;font-weight:700;color:#f3f3f3;margin-bottom:14px}
.footer-col li{list-style:none;font-family:'Quicksand',sans-serif;font-size:16px;font-weight:600;height:34px;display:flex;align-items:center;gap:10px;color:var(--white)}
.footer-col.help li{font-family:'Lato',sans-serif;font-weight:400}
.contact-row{display:flex;align-items:flex-start;gap:14px;font-family:'Quicksand',sans-serif;font-size:17px;font-weight:500;line-height:27px;margin-bottom:20px;color:var(--white)}
.contact-row svg{flex:none;margin-top:-2px}
.footer-rule{position:absolute;left:111px;top:2349px;width:977px;height:1px;background:rgba(255,255,255,.6)}
.copyright{position:absolute;top:2384px;left:0;width:1200px;text-align:center;font-size:16px;color:#f0f0f0}
</style>
</head>
<body>
<div class="rainbow top"></div>

<header class="site-header">
  <a class="nav-link" style="left:109px">Home</a>
  <a class="nav-link" style="left:215px">About</a>
  <a class="nav-link" style="left:323px">Services</a>
  <a class="nav-link" style="left:756px">News</a>
  <a class="nav-link" style="left:861px">Reviews</a>
  <a class="btn-contact">Contact Us</a>
</header>
<div class="brand-badge"><span class="brand-dot"></span><span class="brand-name">Pebbleton</span></div>

<section class="hero" role="img" aria-label="Family of four running hand in hand across a sunny meadow under a blue sky"></section>
<h1 class="hero-title">Welcome to Pebbleton</h1>
<a class="btn-start">Get Started</a>

<h2 class="section-title" style="top:724px">Our Categories</h2>
<span class="tab" style="left:352px;width:145px">Significant Other</span>
<span class="tab active" style="left:533px;width:121px">Children</span>
<span class="tab" style="left:687px;width:160px">Family and Friends</span>

<svg class="arrow" style="left:34px" viewBox="0 0 26 26"><circle cx="13" cy="13" r="13" fill="#111"/><path d="M15 7l-6 6 6 6" stroke="#fff" stroke-width="2.5" fill="none"/></svg>
<svg class="arrow" style="left:1127px" viewBox="0 0 26 26"><circle cx="13" cy="13" r="13" fill="#111"/><path d="M11 7l6 6-6 6" stroke="#fff" stroke-width="2.5" fill="none"/></svg>

<article class="card" style="left:111px">
  <div class="card-photo" role="img" aria-label="Older couple embracing on the grass in a park" style="background:linear-gradient(180deg,#7f9c5a,#a9bb7c 45%,#8fa6c8 75%,#6f8fb9)"></div>
  <div class="card-body"><p class="card-date">JANUARY 31, 2024</p><p class="card-text">Temporibus autem quibusdam et aut officiis debitis aut rerum necessitatibus saepe</p><a class="card-more">READ MORE</a></div>
</article>
<article class="card featured" style="left:454px">
  <div class="card-photo" role="img" aria-label="Parents sitting on a sofa with their two children" style="background:linear-gradient(135deg,#ddd9d2,#9aa3ae 45%,#56647a 75%,#3b4660)"></div>
  <div class="card-body"><p class="card-date">AUGUST 25, 2023</p><p class="card-text">Eveniet ut et voluptates repudiandae sint et voluptatum deleniti atquemolestiae non recusandae</p><a class="card-more">READ MORE</a></div>
</article>
<article class="card" style="left:796px">
  <div class="card-photo" role="img" aria-label="Mother resting her head close to her sleeping son" style="background:linear-gradient(135deg,#3a2a24,#8a5a44 40%,#d9c9bf 70%,#efe9e4)"></div>
  <div class="card-body"><p class="card-date">FEBRUARY 16, 2024</p><p class="card-text">Itaque earum rerum hic tenetur a sapiente delectus, ut aut reiciendis voluptatibus maiores</p><a class="card-more">READ MORE</a></div>
</article>

<section class="news"></section>
<h2 class="section-title" style="top:1430px">Latest News</h2>
<article class="news-main">
  <div class="news-main-photo" role="img" aria-label="Group of people stacking their fists together in a show of unity"></div>
  <p class="news-main-caption">Voluptatibus maiores alias consequatur aut perferendis doloribus</p>
</article>
<article class="news-item" style="top:1509px"><div class="news-thumb" role="img" aria-label="Three generations of a family smiling outdoors" style="background:linear-gradient(135deg,#b9c6b0,#d8c1a8 50%,#4c6e9e)"></div><span class="news-date">09 &nbsp;Feb 2024</span><span class="news-head">At vero eos et accusamus</span><a class="news-more">Read More</a></article>
<article class="news-item" style="top:1630px"><div class="news-thumb" role="img" aria-label="Mother hugging her smiling daughter" style="background:linear-gradient(135deg,#c8a581,#8c6544 50%,#e6e2de)"></div><span class="news-date">19 &nbsp;Jan 2024</span><span class="news-head">At vero eos et accusamus</span><a class="news-more">Read More</a></article>
<article class="news-item" style="top:1751px"><div class="news-thumb" role="img" aria-label="Smiling couple leaning their heads together" style="background:linear-gradient(135deg,#3d2c25,#8b624b 45%,#b8a595 75%,#7d8790)"></div><span class="news-date">24 &nbsp;Feb 2024</span><span class="news-head">At vero eos et accusamus</span><a class="news-more">Read More</a></article>
<article class="news-item" style="top:1872px"><div class="news-thumb" role="img" aria-label="Large group of friends posing together in a forest" style="background:linear-gradient(135deg,#6f5a45,#b48f6e 45%,#7c8a5e 75%,#4c5a3c)"></div><span class="news-date">21 &nbsp;Feb 2024</span><span class="news-head">At vero eos et accusamus</span><a class="news-more">Read More</a></article>

<footer class="site-footer"></footer>
<div class="footer-brand"><span class="dot"></span><span class="name">Pebbleton</span></div>

<nav class="footer-col" style="left:430px">
  <h3>Quick Links</h3>
  <ul>
    <li><svg width="14" height="14" viewBox="0 0 14 14"><path d="M1 7h10M7 2l5 5-5 5" stroke="#fff" stroke-width="2.4" fill="none"/></svg>Home</li>
    <li><svg width="14" height="14" viewBox="0 0 14 14"><path d="M1 7h10M7 2l5 5-5 5" stroke="#fff" stroke-width="2.4" fill="none"/></svg>About</li>
    <li><svg width="14" height="14" viewBox="0 0 14 14"><path d="M1 7h10M7 2l5 5-5 5" stroke="#fff" stroke-width="2.4" fill="none"/></svg>Classes</li>
    <li><svg width="14" height="14" viewBox="0 0 14 14"><path d="M1 7h10M7 2l5 5-5 5" stroke="#fff" stroke-width="2.4" fill="none"/></svg>Testimonials</li>
    <li><svg width="14" height="14" viewBox="0 0 14 14"><path d="M1 7h10M7 2l5 5-5 5" stroke="#fff" stroke-width="2.4" fill="none"/></svg>Contact Us</li>
  </ul>
</nav>
<nav class="footer-col help" style="left:662px">
  <h3>Help Links</h3>
  <ul>
    <li><svg width="14" height="14" viewBox="0 0 14 14"><path d="M1 7h10M7 2l5 5-5 5" stroke="#fff" stroke-width="2.4" fill="none"/></svg>FAQ</li>
    <li><svg width="14" height="14" viewBox="0 0 14 14"><path d="M1 7h10M7 2l5 5-5 5" stroke="#fff" stroke-width="2.4" fill="none"/></svg>Terms of use</li>
    <li><svg width="14" height="14" viewBox="0 0 14 14"><path d="M1 7h10M7 2l5 5-5 5" stroke="#fff" stroke-width="2.4" fill="none"/></svg>Privacy Policy</li>
    <li><svg width="14" height="14" viewBox="0 0 14 14"><path d="M1 7h10M7 2l5 5-5 5" stroke="#fff" stroke-width="2.4" fill="none"/></svg>Support Links</li>
    <li><svg width="14" height="14" viewBox="0 0 14 14"><path d="M1 7h10M7 2l5 5-5 5" stroke="#fff" stroke-width="2.4" fill="none"/></svg>Conditions</li>
  </ul>
</nav>
<address class="footer-col" style="left:914px;font-style:normal">
  <h3>Contact Us</h3>
  <div class="contact-row"><svg width="33" height="33" viewBox="0 0 33 33"><circle cx="16.5" cy="16.5" r="16.5" fill="#fff"/><path d="M16.5 8a6 6 0 0 0-6 6c0 4.5 6 11 6 11s6-6.5 6-11a6 6 0 0 0-6-6z" fill="#0e62a9"/><circle cx="16.5" cy="14" r="2.2" fill="#fff"/></svg><span>Pebbleton Studio<br>United States</span></div>
  <div class="contact-row"><svg width="33" height="33" viewBox="0 0 33 33"><circle cx="16.5" cy="16.5" r="16.5" fill="#fff"/><path d="M11 9.5l3-.5 2 4.5-2 1.5a10 10 0 0 0 4.5 4.5l1.5-2 4.5 2-.5 3c-7 .5-13.5-6-13-13z" fill="#0e62a9"/></svg><span>+1 555 014 2290</span></div>
  <div class="contact-row"><svg width="33" height="33" viewBox="0 0 33 33"><circle cx="16.5" cy="16.5" r="16.5" fill="#fff"/><rect x="9" y="11" width="15" height="11" rx="1.5" fill="#0e62a9"/><path d="M9.5 12l7 5.5 7-5.5" stroke="#fff" stroke-width="1.4" fill="none"/></svg><span>hello@pebbleton.app</span></div>
</address>
<div class="footer-rule"></div>
<p class="copyright">Copyrights@2024.Pebbletonapp.All Rights Reserved</p>

<div class="rainbow bottom"></div>
</body>
</html>
```